I am a Financial Adviser specialising in Aged Care Advice. We provide financial advice and assistance to families with loved ones entering an Aged Care facility.
We need a flyer detailing the Aged Care Packages that we offer. There will be 3 main packages & then other add ons. I need an area where the client can sign off on the package/s that they choose. I have attached a sample to demonstrate the required layout, and a copy of content. I would like the flyer to have an image as per the attached sample, and to be designed in soft pastels, blues, greens.

```html
<!DOCTYPE html>
<html lang="en">
<head>
<meta charset="utf-8">
<title>Aged Care Packages Flyer</title>
<link href="https://fonts.googleapis.com/css2?family=Roboto+Condensed:ital,wght@0,300;0,400;0,700;1,400&display=swap" rel="stylesheet">
<style>
:root{
  --bg:#e9e6e1;
  --paper:#ffffff;
  --blue:#9aa2c7;
  --blue-dark:#7e87b4;
  --olive:#84894a;
  --olive-dark:#6e7338;
  --navy:#2f3470;
  --ink:#2b2b2b;
  --cream:#dcdaa6;
  --gold:#c9a227;
  --photo-a:#a9b768;
  --photo-b:#d9cfa3;
  --hands-a:#c9ab97;
  --hands-b:#8d7462;
}
*{box-sizing:border-box;margin:0;padding:0}
html,body{width:1200px;height:1200px;overflow:hidden;background:var(--bg);font-family:"Roboto Condensed",Arial,sans-serif;color:var(--ink)}
.canvas{position:relative;width:1200px;height:1200px}

/* Options sheet */
.options-sheet{position:absolute;left:65px;top:158px;width:521px;height:675px;background:var(--paper);box-shadow:0 6px 18px rgba(0,0,0,.25);overflow:hidden}
.options-sheet h1{position:absolute;top:26px;left:0;width:100%;text-align:center;font-size:28px;font-weight:700;letter-spacing:.3px;color:#333}
.option{position:absolute;left:51px;width:444px;height:48px;color:#fff;display:flex}
.option.blue{background:var(--blue)}
.option.olive{background:var(--olive)}
.option .label{position:relative;width:116px;height:100%;text-align:center;padding-top:5px}
.option .label .name{display:block;font-size:9.5px;font-weight:700;line-height:11px}
.option .label .price{display:block;font-size:17px;font-weight:700;line-height:20px}
.option .chevron{position:absolute;right:-32px;top:0;width:36px;height:48px}
.option .desc{flex:1;padding:0 14px 0 34px;font-size:9.2px;line-height:12px;font-weight:400;display:flex;align-items:center;text-align:justify}
.tickbox{position:absolute;left:30px;width:13px;height:13px;border:1px solid #999;background:#fff}
.sign-off{position:absolute;left:30px;top:472px;width:466px;font-size:7.4px;line-height:10px;color:#222}
.sign-line{position:absolute;font-size:7.5px;color:#333;letter-spacing:.5px}
.sign-label{position:absolute;font-size:9px;color:#333}
.disclaimer{position:absolute;left:30px;width:466px;font-size:7px;line-height:9.5px;color:#222}
.sheet-foot{position:absolute;left:0;bottom:0;width:100%;height:22px;background:linear-gradient(90deg,#d6d5b3,#eeecd8 60%,#e4e2c6)}

/* Packages sheet */
.packages-sheet{position:absolute;left:630px;top:344px;width:520px;height:676px;background:var(--blue);box-shadow:0 6px 18px rgba(0,0,0,.25);overflow:hidden}
.family-photo{position:absolute;left:0;top:0;width:520px;height:256px;background:linear-gradient(170deg,#e4e3c4 0%,var(--photo-b) 35%,var(--photo-a) 80%,#7f9444 100%)}
.band{position:absolute;left:0;width:520px}
.band.essentials{top:256px;height:128px;background:var(--blue)}
.band.advantage{top:384px;height:142px;background:var(--olive)}
.band.platinum{top:526px;height:150px;background:var(--blue)}
.overlay{position:absolute;left:0;top:0;width:520px;height:676px}
.pkg-head{position:absolute;left:0;width:420px;height:40px;border-bottom:1.5px solid var(--navy)}
.pkg-head.blue{background:var(--blue-dark)}
.pkg-head.olive{background:var(--olive-dark)}
.pkg-box{position:absolute;left:15px;top:5px;width:29px;height:29px;background:#fff;border:1px solid var(--navy)}
.pkg-title{position:absolute;left:51px;top:3px;font-size:17.5px;font-weight:700;color:#fff;white-space:nowrap}
.pkg-sub{position:absolute;left:51px;top:22px;font-size:13px;font-weight:300;color:#fff;white-space:nowrap}
.pkg-list{position:absolute;left:51px;list-style:none;color:#fff;font-size:9.6px;line-height:13.8px}
.pkg-list .lead{font-size:11px;font-weight:700;margin-bottom:1px;line-height:14px}
.pkg-list li.item{padding-left:13px;position:relative}
.pkg-list li.item::before{content:"";position:absolute;left:1px;top:4.5px;width:5px;height:5px;background:#fff}
.pkg-note{position:absolute;left:51px;top:371px;font-size:6.5px;color:#fff}
.pill{position:absolute;height:26px;padding:0 0 0 10px;border-radius:13px 0 0 13px;color:#fff;font-size:16px;font-style:italic;line-height:26px}
.pill.blue{background:var(--blue-dark)}
.pill.olive{background:var(--olive-dark)}
.brand{position:absolute;left:352px;top:292px;display:flex;align-items:center;gap:6px;font-size:15px;font-weight:700;color:#2b2b2b;letter-spacing:.4px}
.brand-dot{width:10px;height:10px;border-radius:50%;background:var(--gold)}
</style>
</head>
<body>
<div class="canvas">

  <section class="options-sheet">
    <h1>EXTRA CHOICE OPTIONS</h1>

    <span class="tickbox" style="top:85px"></span>
    <div class="option blue" style="top:68px">
      <div class="label"><span class="name">Centre Link / DVA Nominee</span><span class="price">$1,100</span>
        <svg class="chevron" viewBox="0 0 36 48"><polyline points="2,0 30,24 2,48" fill="none" stroke="#fff" stroke-width="1.6"/></svg></div>
      <div class="desc">Communicate with CentreLink / DVA on behalf of our client /s, and undertake all changes and updates to details, as directed by our client.</div>
    </div>

    <span class="tickbox" style="top:140px"></span>
    <div class="option olive" style="top:123px">
      <div class="label" style="padding-top:3px"><span class="name">Post Implementation<br>Statement of Advice</span><span class="price">$1,650</span>
        <svg class="chevron" viewBox="0 0 36 48"><polyline points="2,0 30,24 2,48" fill="none" stroke="#fff" stroke-width="1.6"/></svg></div>
      <div class="desc">Revise our original Advice Statement for any changes of circumstances including income &amp; asset variations, and provide further advice within the first 12 months of initial advice statement.</div>
    </div>

    <span class="tickbox" style="top:196px"></span>
    <div class="option blue" style="top:179px">
      <div class="label"><span class="name">Annual Review</span><span class="price">$990</span>
        <svg class="chevron" viewBox="0 0 36 48"><polyline points="2,0 30,24 2,48" fill="none" stroke="#fff" stroke-width="1.6"/></svg></div>
      <div class="desc">A review of the recommendations made in our original advice document, taking into account any changes to client's circumstances includingchecking current cash flow is sufficient to meet ongoing aged care</div>
    </div>

    <span class="tickbox" style="top:252px"></span>
    <div class="option olive" style="top:235px">
      <div class="label"><span class="name">Post Entry Review</span><span class="price">$660</span>
        <svg class="chevron" viewBox="0 0 36 48"><polyline points="2,0 30,24 2,48" fill="none" stroke="#fff" stroke-width="1.6"/></svg></div>
      <div class="desc">Review financial situation, check facility invoices are accurate, explain the Residential Aged Care Agreement and ensure all recommendations are implemented.</div>
    </div>

    <span class="tickbox" style="top:307px"></span>
    <div class="option blue" style="top:290px">
      <div class="label"><span class="name">Facility Liason</span><span class="price">$550</span>
        <svg class="chevron" viewBox="0 0 36 48"><polyline points="2,0 30,24 2,48" fill="none" stroke="#fff" stroke-width="1.6"/></svg></div>
      <div class="desc">Negotiate with the Aged Care Facility regarding Accommodation payments, clarify &amp; explain Residential Care Agreement, and review facility invoices.</div>
    </div>

    <span class="tickbox" style="top:363px"></span>
    <div class="option olive" style="top:346px">
      <div class="label"><span class="name">Family Conferences</span><span class="price">$660</span>
        <svg class="chevron" viewBox="0 0 36 48"><polyline points="2,0 30,24 2,48" fill="none" stroke="#fff" stroke-width="1.6"/></svg></div>
      <div class="desc">Facilitate &amp; co-ordinate family meetings to explain the Aged Care legislation and how it fits with the family circumstances.</div>
    </div>

    <span class="tickbox" style="top:418px"></span>
    <div class="option blue" style="top:401px">
      <div class="label"><span class="name">Family Conferences</span><span class="price">$660</span>
        <svg class="chevron" viewBox="0 0 36 48"><polyline points="2,0 30,24 2,48" fill="none" stroke="#fff" stroke-width="1.6"/></svg></div>
      <div class="desc">Facilitate &amp; co-ordinate family meetings to explain the Aged Care legislation and how it fits with the family circumstances.</div>
    </div>

    <p class="sign-off">I/We have chosen the Service Package and Options as ticked above.&nbsp; I/We understand that by choosing the Essentials Package, that I/We are receiving factual information only, and not financial advice.&nbsp; I/We agree to<br>pay the amount of ………………….., within seven days of the date of the invoice received from Silverleaf Advisory SA.</p>

    <span class="sign-line" style="left:30px;top:516px">…………………………………………</span>
    <span class="sign-line" style="left:174px;top:516px">…………………………………………</span>
    <span class="sign-line" style="left:300px;top:516px">…………………………………………</span>
    <span class="sign-line" style="left:420px;top:516px">……/………/………</span>
    <span class="sign-label" style="left:74px;top:530px">Signature</span>
    <span class="sign-label" style="left:256px;top:530px">Signature Signature</span>
    <span class="sign-label" style="left:442px;top:530px">Date</span>
    <span class="sign-line" style="left:30px;top:556px">…………………………………………</span>
    <span class="sign-line" style="left:172px;top:556px">………/………/………</span>
    <span class="sign-label" style="left:66px;top:570px">Adviser Signature</span>
    <span class="sign-label" style="left:206px;top:570px">Date</span>

    <p class="disclaimer" style="top:591px">This document has been prepared by Silverleaf Advisory SA Pty Ltd ABN 12 345 678 901, an Authorised Representative of Prudent Path Limited ABN 98 765 432 109 AFSL 400123, a wholly owned, non-guaranteed subsidiary of the Southern Cross Mutual Bank ABN 55 111 222 333.</p>
    <p class="disclaimer" style="top:615px">Information in this document is based on current regulatory requirements and laws, as at 20 September, 2016 which may be subject to change. It contains general advice. It does not take into account your individual objectives, financial situation or needs. You should consider talking to a financial adviser before making a financial decision.</p>
    <div class="sheet-foot"></div>
  </section>

  <section class="packages-sheet">
    <div class="family-photo" role="img" aria-label="Photo of a smiling multi-generation family sitting together on grass outdoors"></div>
    <div class="band essentials"></div>
    <div class="band advantage"></div>
    <div class="band platinum"></div>

    <svg class="overlay" viewBox="0 0 520 676" aria-hidden="true">
      <defs>
        <linearGradient id="handsTone" x1="0" y1="0" x2="1" y2="1">
          <stop offset="0" stop-color="var(--hands-a)"/>
          <stop offset="1" stop-color="var(--hands-b)"/>
        </linearGradient>
      </defs>
      <polygon points="274,256 520,256 520,312 441,384 394,384" fill="#fff"/>
      <polygon points="520,312 270,540 410,676 520,676" fill="var(--cream)"/>
      <polygon points="520,322 280,540 415,676 520,676" fill="#fff"/>
    </svg>
    <svg class="overlay" viewBox="0 0 520 676" role="img" aria-label="Photo of an elderly hand held gently in a younger hand">
      <polygon points="520,330 290,540 420,676 520,676" fill="url(#handsTone)"/>
    </svg>

    <div class="brand"><span class="brand-dot"></span>Silverleaf Advisory</div>

    <div class="pkg-head blue" style="top:256px;width:274px;clip-path:polygon(0 0,85% 0,100% 100%,0 100%)">
      <span class="pkg-box"></span>
      <span class="pkg-title">ESSENTIALS Package $770</span>
      <span class="pkg-sub">When you know what you want....</span>
    </div>
    <ul class="pkg-list" style="top:298px">
      <li class="item">Explanation of Aged Care Fees and Charges.</li>
      <li class="item">Preliminary Home / Assets Assessment.*</li>
      <li class="item">Estimated Means Tested Fee Calculation.*</li>
      <li class="item">Preliminary Aged Care Costs.*</li>
      <li class="item">Estimated Cash Flow Scenario.*</li>
    </ul>
    <p class="pkg-note">*Please note this is general factual information only.&nbsp; We do not provide any specific personal information.</p>
    <div class="pill blue" style="left:225px;top:334px;width:126px">Peace of Mind</div>

    <div class="pkg-head olive" style="top:384px;width:395px;clip-path:polygon(0 0,88% 0,100% 100%,0 100%)">
      <span class="pkg-box"></span>
      <span class="pkg-title">ADVANTAGE Package $2,970</span>
      <span class="pkg-sub">When you need to know all the options....</span>
    </div>
    <ul class="pkg-list" style="top:426px">
      <li class="lead">Essentials Package Plus</li>
      <li class="item">Analyse and Strategize Aged Care costs.</li>
      <li class="item">Compare up to 5 Strategy options.</li>
      <li class="item">Minimise Aged Care Costs (where possible).</li>
      <li class="item">Maximise Age Pension Income (where possible).</li>
      <li class="item">Prepare a Full Statement of Advice (SOA).</li>
      <li class="item">Implementation of Aged Care Strategy.</li>
    </ul>
    <div class="pill olive" style="left:222px;top:438px;width:200px">Confidence</div>

    <div class="pkg-head blue" style="top:526px;width:270px;clip-path:polygon(0 0,100% 0,92% 100%,0 100%)">
      <span class="pkg-box"></span>
      <span class="pkg-title">PLATINUM Package $5,940</span>
      <span class="pkg-sub">When you need someone to take charge</span>
    </div>
    <ul class="pkg-list" style="top:567px">
      <li class="lead">Advantage Packageplus</li>
      <li class="item">Liase with the Aged Care Facility.</li>
      <li class="item">CentreLink/DVA Nominee.</li>
      <li class="item">Post Entry Review.</li>
      <li class="item">Post Implementation SOA (if required).</li>
      <li class="item">Annual Review.</li>
    </ul>
    <div class="pill blue" style="left:223px;top:590px;width:126px">Convenience</div>
  </section>

</div>
</body>
</html>
```